Bramfield Animal Hospital brochure

We have found that our current clients do not know all of the services that we offer so we want to make a hospital brochure to make our services more known. Our website has all of our services listed but we find that clients aren't looking at our website as much as we would like so we are hoping a hospital brochure can sum up our main services and maybe lead to more people visiting our website. Our hospital colors are blue and maroon and our moto is "Outstanding Medicine, Extraordinary Service." Some of the service we would like to promote more include digital x-ray, ultrasounds, echocardiograms, laser therapy and dentals. We also offer after hours emergency care but only to our current clients. You can find more services listed on our website We are in a small town so we want a personal yet professional feel.

Feel free to visit our website to get a better feel for our business https://thecorvelpets.com/

• 6-8 panel brochure
• I included some photos from around the hospital. If you feel that you can make a few work in the brochure then great but don't feel obligated to.

```html
<!DOCTYPE html>
<html lang="en">
<head>
<meta charset="utf-8">
<title>Bramfield Animal Hospital Brochure</title>
<link href="https://fonts.googleapis.com/css2?family=Oswald:wght@200;300;600;700&family=Questrial&display=swap" rel="stylesheet">
<style>
:root{
  --maroon:#8b1c21;
  --maroon-dark:#6e1216;
  --ink:#222;
  --paper:#fff;
  --map-green:#bfe3c6;
}
*{margin:0;padding:0;box-sizing:border-box}
html,body{width:1200px;height:1185px;overflow:hidden;background:var(--paper)}
body{position:relative;font-family:"Questrial",Arial,sans-serif;color:var(--ink)}
.spread{position:absolute;left:190px;width:868px;height:615px;transform:scale(.945);transform-origin:0 0;background:var(--paper);overflow:hidden}
.spread--outside{top:8px}
.spread--inside{top:597px}
.band{position:absolute;left:0;width:868px;height:17px;background:var(--maroon)}
.band--top{top:0}
.band--bottom{top:598px}
.photo{position:absolute}
.body-copy{position:absolute;font-size:10.3px;line-height:13.6px;text-align:justify;hyphens:auto}
.headline{position:absolute;font-family:"Oswald",Arial Narrow,sans-serif;color:var(--maroon);text-transform:uppercase;line-height:1;white-space:nowrap}
.headline__hours{font-weight:700;font-size:74px;letter-spacing:-1px;display:block;transform:scaleX(.92);transform-origin:left}
.headline__care{font-weight:200;font-size:44px;display:block;margin-top:2px;transform:scaleX(.84);transform-origin:left}
.map-frame{position:absolute;left:351px;top:400px;width:167px;height:110px;border:3px solid var(--maroon);border-radius:8px;background:var(--map-green);overflow:hidden}
.contact{position:absolute;left:344px;top:521px;width:180px;text-align:center;font-size:10.5px;line-height:14px}
.contact__icons{display:flex;justify-content:center;gap:2px;margin-bottom:3px}
.logo-box{position:absolute;left:625px;top:393px;width:194px;height:125px;background:var(--paper);border:3px solid var(--maroon);border-radius:9px;display:flex;flex-direction:column;align-items:center;justify-content:center;gap:8px}
.logo-box__mark{width:30px;height:30px;border-radius:50%;background:var(--maroon)}
.logo-box__name{font-family:"Questrial",Arial,sans-serif;color:var(--maroon);font-size:19px;line-height:20px;text-align:center;text-transform:uppercase}
.tagline{position:absolute;left:572px;top:530px;width:300px;text-align:center;white-space:nowrap;font-family:"Oswald",Arial Narrow,sans-serif;font-weight:600;color:var(--maroon);font-size:24px;line-height:28px;text-transform:uppercase;transform:scaleX(.86);transform-origin:center}
.services__title{position:absolute;left:23px;top:322px;font-family:"Oswald",Arial Narrow,sans-serif;font-weight:600;font-size:25px;color:var(--maroon);transform:scaleX(.86);transform-origin:left;white-space:nowrap}
.service{position:absolute;display:flex;align-items:center;gap:8px;font-size:10.8px;line-height:13px;width:125px;white-space:nowrap}
.service__icon{flex:0 0 33px;width:33px;height:33px}
</style>
</head>
<body>

<section class="spread spread--outside" aria-label="Brochure outside">
  <div class="band band--top"></div>
  <p class="body-copy" style="left:25px;top:38px;width:239px">We built Bramfield Animal Hospital for you. It is so important to us that you can walk into an environment where you feel you are always put first, and where the little things have been thought of to make this a truly wonderful experience. We want to make your life easier. We offer evening hours, drop-offs, and house call appointments. And existing clients get access to 24 hour emergency care. Because we are always looking out for you.</p>
  <div class="photo" role="img" aria-label="Photo of a dog running on green grass" style="left:25px;top:185px;width:239px;height:151px;background:linear-gradient(180deg,#7f9a52 0%,#5c8a2e 55%,#4f8a24 100%)"></div>
  <h2 class="headline" style="left:25px;top:352px"><span class="headline__hours">24 Hour</span><span class="headline__care">Emergency Care</span></h2>
  <p class="body-copy" style="left:25px;top:480px;width:239px">We keep a veterinarian on call 24 hours a day for emergency services. In order to treat your pet as quickly as possible, we restrict after hours emergency care to current clients. If you are not a current client and may be experiencing an after hours pet emergency, please contact your regular veterinarian or Valley Regional Animal Emergency Clinic at (518) 555-0172.</p>
  <div class="photo" role="img" aria-label="Photo of a golden retriever and a grey cat resting together" style="left:290px;top:17px;width:578px;height:438px;background:linear-gradient(110deg,#d9d6d2 0%,#b7b2ae 35%,#a87a4c 60%,#c98f55 80%,#e3dcd3 100%)"></div>
  <div class="map-frame" role="img" aria-label="Street map showing the hospital location"></div>
  <div class="contact">
    <div class="contact__icons">
      <svg width="11" height="11" viewBox="0 0 12 12"><circle cx="6" cy="6" r="5.3" fill="none" stroke="#8b1c21"/><path d="M4 3.5l1 1-.6.8c.4.8 1 1.4 1.8 1.8l.8-.6 1 1-.9.9C5.4 8.2 3.8 6.6 3.4 4.4z" fill="#8b1c21"/></svg>
      <svg width="11" height="11" viewBox="0 0 12 12"><circle cx="6" cy="6" r="5.3" fill="none" stroke="#8b1c21"/><rect x="3.3" y="4.2" width="5.4" height="3.6" fill="none" stroke="#8b1c21" stroke-width=".8"/><path d="M3.3 4.2L6 6.3l2.7-2.1" fill="none" stroke="#8b1c21" stroke-width=".8"/></svg>
      <svg width="11" height="11" viewBox="0 0 12 12"><circle cx="6" cy="6" r="5.3" fill="none" stroke="#8b1c21"/><circle cx="6" cy="6" r="2.8" fill="none" stroke="#8b1c21" stroke-width=".8"/><path d="M3.2 6h5.6M6 3.2v5.6" stroke="#8b1c21" stroke-width=".7"/></svg>
    </div>
    802-555-0148<br>info@thecorvelpets.com<br>info@thecorvelpets.com
  </div>
  <div class="logo-box">
    <div class="logo-box__mark"></div>
    <div class="logo-box__name">Bramfield<br>Animal Hospital</div>
  </div>
  <p class="tagline">Outstanding Medicine<br>Extraordinary Service</p>
  <div class="band band--bottom"></div>
</section>

<section class="spread spread--inside" aria-label="Brochure inside">
  <div class="photo" role="img" aria-label="Photo of an orange cat lying on a grey blanket" style="left:0;top:0;width:580px;height:263px;background:linear-gradient(120deg,#6f716c 0%,#8a8b85 30%,#c07a3e 55%,#a9662f 75%,#5f625e 100%)"></div>
  <h2 class="headline" style="left:604px;top:16px"><span class="headline__hours">24 Hour</span><span class="headline__care">Emergency Care</span></h2>
  <p class="body-copy" style="left:604px;top:140px;width:242px">We keep a veterinarian on call 24 hours a day for emergency services. In order to treat your pet as quickly as possible, we restrict after hours emergency care to current clients. If you are not a current client and may be experiencing an after hours pet emergency, please contact your regular veterinarian or Valley Regional Animal Emergency Clinic at (518) 555-0172.</p>
  <div class="band" style="top:263px"></div>
  <div class="photo" role="img" aria-label="Photo of the veterinarian kneeling outdoors with two dogs" style="left:580px;top:280px;width:288px;height:318px;background:linear-gradient(180deg,#2d3a2c 0%,#3e4a3a 45%,#b08a55 70%,#dcdcdc 100%)"></div>

  <h3 class="services__title">SERVICES WE OFFER</h3>

  <svg width="0" height="0" style="position:absolute">
    <defs>
      <symbol id="ring" viewBox="0 0 34 34"><circle cx="17" cy="17" r="15.5" fill="none" stroke="#8b1c21" stroke-width="1.4"/><circle cx="17" cy="17" r="13" fill="none" stroke="#8b1c21" stroke-width=".5"/></symbol>
    </defs>
  </svg>

  <div class="service" style="left:22px;top:373px"><svg class="service__icon" viewBox="0 0 34 34"><use href="#ring"/><path d="M17 23l-6-6a3.3 3.3 0 0 1 6-3.5 3.3 3.3 0 0 1 6 3.5z" fill="#8b1c21"/></svg><span>Cardiology<br>Care</span></div>
  <div class="service" style="left:22px;top:417px"><svg class="service__icon" viewBox="0 0 34 34"><use href="#ring"/><circle cx="17" cy="17" r="4" fill="none" stroke="#8b1c21" stroke-width="1.3"/><path d="M17 9v3M17 22v3M9 17h3M22 17h3" stroke="#8b1c21" stroke-width="1.3"/></svg><span>Cold Laser<br>Therapy</span></div>
  <div class="service" style="left:22px;top:461px"><svg class="service__icon" viewBox="0 0 34 34"><use href="#ring"/><rect x="12" y="10" width="10" height="14" rx="2" fill="#8b1c21"/><path d="M14 14h6M14 17h6M14 20h6" stroke="#fff" stroke-width="1"/></svg><span>Digital<br>X-Ray</span></div>
  <div class="service" style="left:22px;top:505px"><svg class="service__icon" viewBox="0 0 34 34"><use href="#ring"/><path d="M17 10v14M11 13.5l12 7M11 20.5l12-7" stroke="#8b1c21" stroke-width="3"/></svg><span>Emergency<br>Care</span></div>

  <div class="service" style="left:145px;top:373px"><svg class="service__icon" viewBox="0 0 34 34"><use href="#ring"/><circle cx="17" cy="17" r="7" fill="none" stroke="#8b1c21" stroke-width="1.3"/><path d="M12 12l10 10" stroke="#8b1c21" stroke-width="1.3"/></svg><span>Flea and<br>Tick Prevention</span></div>
  <div class="service" style="left:145px;top:417px"><svg class="service__icon" viewBox="0 0 34 34"><use href="#ring"/><path d="M14 10h6v4h4v6h-4v4h-6v-4h-4v-6h4z" fill="#8b1c21"/></svg><span>Heartworm<br>Preventative</span></div>
  <div class="service" style="left:145px;top:461px"><svg class="service__icon" viewBox="0 0 34 34"><use href="#ring"/><path d="M9 18l8-7 8 7M11 17v7h12v-7" fill="none" stroke="#8b1c21" stroke-width="1.6"/><rect x="15" y="19" width="4" height="5" fill="#8b1c21"/></svg><span>In-House<br>Laboratory</span></div>
  <div class="service" style="left:145px;top:505px"><svg class="service__icon" viewBox="0 0 34 34"><use href="#ring"/><rect x="11" y="15" width="12" height="5" rx="2" fill="none" stroke="#8b1c21" stroke-width="1.3"/><path d="M23 17.5h3" stroke="#8b1c21" stroke-width="1.3"/></svg><span>Micro-<br>chipping</span></div>

  <div class="service" style="left:300px;top:343px"><svg class="service__icon" viewBox="0 0 34 34"><use href="#ring"/><path d="M17 23l-6-6a3.3 3.3 0 0 1 6-3.5 3.3 3.3 0 0 1 6 3.5z" fill="none" stroke="#8b1c21" stroke-width="1.4"/></svg><span>End-Of-Life<br>Care</span></div>
  <div class="service" style="left:300px;top:388px"><svg class="service__icon" viewBox="0 0 34 34"><use href="#ring"/><circle cx="17" cy="17" r="4" fill="#8b1c21"/><path d="M11 11l3 3M23 11l-3 3M11 23l3-3M23 23l-3-3" stroke="#8b1c21" stroke-width="1.3"/></svg><span>Parasite<br>Testing</span></div>
  <div class="service" style="left:300px;top:433px"><svg class="service__icon" viewBox="0 0 34 34"><use href="#ring"/><rect x="10" y="12" width="14" height="10" rx="1" fill="none" stroke="#8b1c21" stroke-width="1.3"/><path d="M12 19l3-3 2 2 3-4 2 2" fill="none" stroke="#8b1c21" stroke-width="1"/></svg><span>Allergy and<br>Dermatology</span></div>
  <div class="service" style="left:300px;top:478px"><svg class="service__icon" viewBox="0 0 34 34"><use href="#ring"/><path d="M12 21c0-5 3-9 8-9l2 2-3 1c0 4-2 7-7 6z" fill="none" stroke="#8b1c21" stroke-width="1.3"/></svg><span>Avian<br>Care</span></div>
  <div class="service" style="left:300px;top:523px"><svg class="service__icon" viewBox="0 0 34 34"><use href="#ring"/><path d="M17 9v16M13 13h8M13 21h8" stroke="#8b1c21" stroke-width="1.6"/><circle cx="17" cy="17" r="2.5" fill="#8b1c21"/></svg><span>Senior<br>Wellness</span></div>

  <div class="service" style="left:422px;top:343px"><svg class="service__icon" viewBox="0 0 34 34"><use href="#ring"/><ellipse cx="17" cy="17" rx="4" ry="7" fill="none" stroke="#8b1c21" stroke-width="1.3"/><path d="M17 10v14" stroke="#8b1c21" stroke-width="1"/></svg><span>Nutritional<br>Consultations</span></div>
  <div class="service" style="left:422px;top:388px"><svg class="service__icon" viewBox="0 0 34 34"><use href="#ring"/><circle cx="15" cy="15" r="3" fill="none" stroke="#8b1c21" stroke-width="1.1"/><circle cx="20" cy="20" r="3" fill="none" stroke="#8b1c21" stroke-width="1.1"/></svg><span>Puppy and<br>Kitten Care</span></div>
  <div class="service" style="left:422px;top:433px"><svg class="service__icon" viewBox="0 0 34 34"><use href="#ring"/><path d="M20 10l4 4-9 9h-4v-4z" fill="none" stroke="#8b1c21" stroke-width="1.4"/></svg><span>Blood Tests and<br>Urine Screening</span></div>
  <div class="service" style="left:422px;top:478px"><svg class="service__icon" viewBox="0 0 34 34"><use href="#ring"/><path d="M12 11c2-1 4 0 5 1 1-1 3-2 5-1 1 3-1 5-1 8 0 3-1 5-2 5l-2-5-2 5c-1 0-2-2-2-5 0-3-2-5-1-8z" fill="#8b1c21"/></svg><span>Canine and Feline<br>Dental Care</span></div>
  <div class="service" style="left:422px;top:523px"><svg class="service__icon" viewBox="0 0 34 34"><use href="#ring"/><rect x="10" y="18" width="14" height="5" rx="1" fill="none" stroke="#8b1c21" stroke-width="1.3"/><circle cx="17" cy="13" r="3" fill="none" stroke="#8b1c21" stroke-width="1.3"/></svg><span>Soft Tissue<br>Surgery</span></div>

  <div class="band band--bottom"></div>
</section>

</body>
</html>
```